Business card for event manager / organizer "velmora tandem"

Draft of a new valuable business card for my company.
Events, personnel service providers, festivals

```html
<!DOCTYPE html>
<html lang="de">
<head>
<meta charset="utf-8">
<title>Velmora Tandem – Visitenkarte</title>
<link rel="stylesheet" href="https://fonts.googleapis.com/css2?family=Open+Sans:wght@300;600;700&display=swap">
<style>
  :root {
    --stage: #6e6f73;
    --card: #0a0a0b;
    --gold: #b7986a;
    --gold-muted: #8c7a62;
    --white: #ffffff;
    --soft: #cfcfcf;
  }
  * { box-sizing: border-box; margin: 0; padding: 0; }
  html, body { width: 1200px; height: 1200px; overflow: hidden; }
  body {
    background: var(--stage);
    font-family: "Open Sans", Arial, sans-serif;
    position: relative;
  }
  .card {
    position: absolute;
    background: var(--card);
    border-radius: 28px;
    overflow: hidden;
  }
  .card--front { left: 223px; top: 104px; width: 755px; height: 431px; }
  .card--back { left: 215px; top: 658px; width: 760px; height: 436px; }

  .brand {
    position: absolute;
    left: 0; right: 0; top: 170px;
    display: flex; align-items: center; justify-content: center; gap: 14px;
    white-space: nowrap;
  }
  .brand__mark { width: 34px; height: 34px; background: var(--gold); flex: none; }
  .brand__name {
    color: var(--white); font-weight: 700; font-size: 40px;
    letter-spacing: 1px; text-transform: uppercase;
  }
  .tagline {
    position: absolute; left: 0; right: 0; top: 250px;
    text-align: center; color: var(--soft);
    font-weight: 300; font-size: 12px; padding-left: 80px;
    white-space: nowrap;
  }
  .front-url {
    position: absolute; left: 0; right: 0; bottom: 22px;
    text-align: center; color: var(--gold-muted);
    font-weight: 700; font-size: 14px; letter-spacing: 4px;
    white-space: nowrap;
  }

  .back-brand {
    position: absolute; left: 612px; top: 44px;
    display: flex; align-items: center; gap: 6px;
    white-space: nowrap;
  }
  .back-brand__mark { width: 14px; height: 14px; background: var(--gold); flex: none; }
  .back-brand__name {
    color: var(--white); font-weight: 700; font-size: 11px; text-transform: uppercase;
  }
  .portrait {
    position: absolute; left: 76px; top: 102px;
    width: 226px; height: 226px; border-radius: 50%;
    border: 3px solid var(--gold);
    background: radial-gradient(circle at 50% 40%, #6a6a6c 0%, #3b3b3d 55%, #1c1c1e 100%);
  }
  .divider {
    position: absolute; left: 324px; top: 91px;
    width: 2px; height: 231px; background: var(--gold);
  }
  .person { position: absolute; left: 352px; top: 98px; }
  .person__name { color: var(--white); font-weight: 700; font-size: 23px; line-height: 1.1; white-space: nowrap; }
  .person__role {
    display: inline-block; margin-top: 2px; margin-left: 4px;
    color: var(--gold); font-weight: 700; font-size: 17px; letter-spacing: 4px;
    border-bottom: 1.5px solid var(--gold); line-height: 1.2;
  }
  .contacts { position: absolute; left: 352px; top: 161px; list-style: none; }
  .contact {
    position: absolute; left: 0; display: flex; align-items: center; width: 380px;
  }
  .contact svg { width: 29px; height: 29px; flex: none; }
  .contact__text {
    margin-left: 24px; color: var(--gold); font-weight: 700; font-size: 12.5px;
    line-height: 1.25; text-transform: uppercase; white-space: nowrap;
  }
  .band {
    position: absolute; left: 0; right: 0; bottom: 0; height: 39px; background: var(--gold);
  }
</style>
</head>
<body>
  <section class="card card--front">
    <div class="brand">
      <span class="brand__mark"></span>
      <span class="brand__name">Velmora Tandem</span>
    </div>
    <p class="tagline">..damit Ihr nächstes Event sicher gelingt!</p>
    <p class="front-url">WWW.VELMORA-TANDEM.DE</p>
  </section>

  <section class="card card--back">
    <div class="back-brand">
      <span class="back-brand__mark"></span>
      <span class="back-brand__name">Velmora Tandem</span>
    </div>
    <div class="portrait" role="img" aria-label="Porträtfoto des Inhabers"></div>
    <div class="divider"></div>
    <div class="person">
      <h1 class="person__name">JONAS RELING</h1>
      <p class="person__role">INHABER</p>
    </div>
    <ul class="contacts">
      <li class="contact" style="top:0">
        <svg viewBox="0 0 30 30"><circle cx="15" cy="15" r="13.5" fill="none" stroke="#b7986a" stroke-width="1.5"/><path d="M10.5 8.5l2.5 0 1.2 3.2-1.6 1.3c.8 1.8 2.3 3.3 4.1 4.1l1.3-1.6 3.2 1.2v2.5c0 .8-.7 1.4-1.5 1.3-5.2-.5-9.3-4.6-9.8-9.8-.1-.8.5-1.5 1.3-1.5z" fill="none" stroke="#b7986a" stroke-width="1.3"/></svg>
        <span class="contact__text">02360 100 20 30<br>0170 000 11 22</span>
      </li>
      <li class="contact" style="top:34px">
        <svg viewBox="0 0 30 30"><circle cx="15" cy="15" r="13.5" fill="none" stroke="#b7986a" stroke-width="1.5"/><g fill="none" stroke="#b7986a" stroke-width="1.2"><circle cx="15" cy="15" r="7.5"/><ellipse cx="15" cy="15" rx="3.2" ry="7.5"/><path d="M7.5 15h15M8.6 11h12.8M8.6 19h12.8"/></g></svg>
        <span class="contact__text">WWW.VELMORA-TANDEM.DE</span>
      </li>
      <li class="contact" style="top:69px">
        <svg viewBox="0 0 30 30"><circle cx="15" cy="15" r="13.5" fill="none" stroke="#b7986a" stroke-width="1.5"/><g fill="none" stroke="#b7986a" stroke-width="1.2"><path d="M8 13l7-5 7 5v8H8z"/><path d="M8 13l7 5 7-5"/></g></svg>
        <span class="contact__text">INFO@VELMORA-TANDEM.DE</span>
      </li>
      <li class="contact" style="top:104px">
        <svg viewBox="0 0 30 30"><circle cx="15" cy="15" r="13.5" fill="none" stroke="#b7986a" stroke-width="1.5"/><path d="M8 15l7-6.5 7 6.5h-2v6h-3.5v-4h-3v4H10v-6z" fill="#b7986a"/></svg>
        <span class="contact__text">LINDENWEG 12, 40210<br>MUSTERSTADT</span>
      </li>
      <li class="contact" style="top:138px">
        <svg viewBox="0 0 30 30"><circle cx="15" cy="15" r="13.5" fill="none" stroke="#b7986a" stroke-width="1.5"/><circle cx="15" cy="15" r="4" fill="#b7986a"/></svg>
        <span class="contact__text">@VELMORATANDEM</span>
      </li>
    </ul>
    <div class="band"></div>
  </section>
</body>
</html>
```